Website Design for an Exciting & Sophisticated Premium CBD Company.

Design a responsive Website with the following goals in mind:
-      Main theme for the site will be based on the Vendora Lattice Tidemark theme.  Please use this when designing for ease of integration.  You can see our current site to gain more insight.  zellocbd.com
-	Build trust with website visitors with an engaging, informative content driven website, that leads to a conversion of product purchase and repeat business.
-	The website will embody a lifestyle feel and make the visitor identify with the content or emphasize with the life they used to have or believe they can have by using our products
-	The website will allow for super charged SEO and other digital marketing and advertising strategies and tactics used to increase discovery, awareness, and conversion.
Please see additional goals in the uploaded files.

Target Market(s)
Male/Female 25-50
Number of Pages Required
1 page
Font styles to use
Other font styles liked:
- Monserrat is the company Font. Please use throughout. Regular, Bold, Semi-Bold, light
Requirements
Must have
- Please see attached document for this information
Nice to have
Should not have

```html
<!DOCTYPE html>
<html lang="en">
<head>
<meta charset="utf-8">
<title>Zello CBD</title>
<link href="https://fonts.googleapis.com/css2?family=Montserrat:wght@300;400;500;600;700&display=swap" rel="stylesheet">
<style>
:root{
  --gold:#e9c86a;
  --gold-deep:#d9ae3f;
  --cream:#f7f1e1;
  --ink:#2d2d2d;
  --muted:#8a8a8a;
  --line:#e4e4e4;
  --white:#ffffff;
  --bottle:#1f1f1f;
}
*{box-sizing:border-box;margin:0;padding:0}
html,body{width:1200px;height:5012px;overflow:hidden}
body{font-family:'Montserrat',sans-serif;color:var(--ink);background:var(--white);position:relative}
.section{position:absolute;left:0;width:1200px}
.title{font-size:36px;font-weight:300;text-align:center;color:var(--ink)}
.title b{color:var(--gold);font-weight:600}
.btn{display:inline-block;background:var(--gold);color:var(--white);font-weight:600;font-size:14px;letter-spacing:1px;border-radius:22px;padding:12px 30px;text-transform:uppercase}

/* top bar + nav */
.topbar{top:0;height:32px;background:var(--gold);color:var(--white);font-size:12px;text-align:center;line-height:32px}
.nav{top:32px;height:80px;background:var(--white);display:flex;align-items:center;justify-content:space-between;padding:0 110px;font-size:13px;font-weight:600;letter-spacing:1px}
.nav .links{display:flex;gap:34px}
.nav .links .active{border-bottom:2px solid var(--gold);padding-bottom:6px}
.logo{position:absolute;left:50%;transform:translateX(-50%);display:flex;align-items:center;gap:8px;font-size:20px;font-weight:700;color:var(--gold-deep);letter-spacing:2px}
.logo i{width:14px;height:14px;border-radius:50%;background:var(--gold)}

/* hero */
.hero{top:112px;height:548px;background:linear-gradient(90deg,#eef0e9 0%,#e3e8dc 22%,#eceae3 42%,#e2d6c8 62%,#c9ad93 80%,#a98a70 100%)}
.hero-copy{position:absolute;left:170px;top:170px;width:320px;text-align:center}
.hero-copy small{font-size:18px;font-weight:500;letter-spacing:2px;display:block;color:var(--ink)}
.hero-copy h1{font-size:44px;font-weight:700;letter-spacing:2px;margin:6px 0 24px;color:var(--ink)}

/* about company */
.about{top:660px;height:500px;background:#fbf9f3}
.about .shot{position:absolute;left:0;top:0;width:600px;height:500px;background:radial-gradient(ellipse 180px 200px at 230px 290px,#2b2b2b 0%,#3a352c 55%,rgba(240,235,222,0) 100%),linear-gradient(135deg,#f6f3ea,#e6dfcd)}
.about .text{position:absolute;left:690px;top:105px;width:420px}
.about h2{font-size:38px;font-weight:600;color:var(--gold);line-height:1.15}
.about h2 span{color:var(--gold-deep)}
.about p{font-size:13px;line-height:1.7;color:#666;margin-top:18px}

/* brand */
.brand{top:1168px;height:444px;background:var(--gold)}
.brand .shot{position:absolute;right:0;top:0;width:700px;height:444px;background:radial-gradient(ellipse 120px 160px at 520px 250px,#e9c352 0%,rgba(233,195,82,0) 100%),linear-gradient(90deg,#e9c86a 0%,#9aa36c 35%,#56703f 60%,#2f3f2a 100%)}
.brand .text{position:absolute;left:120px;top:100px;width:300px;color:var(--white)}
.brand h2{font-size:32px;font-weight:300}
.brand h2 b{font-weight:700}
.brand p{font-size:13px;line-height:1.75;margin-top:14px}

/* featured */
.featured{top:1720px;height:420px}
.products{display:flex;gap:26px;justify-content:center;margin-top:48px}
.card{width:218px;text-align:center}
.card .pic{height:236px;border:1px solid var(--line);position:relative;display:flex;align-items:flex-end;justify-content:center;background:radial-gradient(ellipse 40px 80px at 50% 48%,#1f1f1f 0%,#2e2a22 60%,rgba(255,255,255,0) 100%),#ffffff}
.stars{color:var(--gold);font-size:13px;margin-top:12px;letter-spacing:1px}
.stars em{color:var(--muted);font-style:normal;font-size:11px}
.card h4{font-size:14px;font-weight:600;margin-top:4px}
.card p{font-size:12px;color:var(--muted)}
.card .price{color:var(--gold);font-weight:600;font-size:16px;margin-top:4px}
.card .btn{font-size:11px;padding:9px 20px;margin-bottom:18px}
.arrow{position:absolute;top:250px;font-size:32px;color:var(--ink);font-weight:300}

/* why */
.why{top:2320px;height:620px;background:linear-gradient(180deg,#fbfbfb,#f4f4f4)}
.feat{position:absolute;display:flex;align-items:center;gap:16px;font-size:13px;font-weight:600;width:300px}
.feat.left{justify-content:flex-end;text-align:right}
.dot{width:48px;height:48px;border-radius:50%;background:var(--gold);flex:none}
.dot.dark{background:#555}

/* reviews */
.reviews{top:3040px;height:560px}
.quote{position:absolute;left:130px;top:110px;width:640px}
.quote .mark{font-size:90px;color:var(--gold);line-height:.6;position:absolute;left:-10px;top:10px}
.quote h3{font-size:30px;font-weight:600;margin-left:50px}
.quote p{font-size:13px;color:#666;line-height:1.7;margin:16px 0 0 50px}
.quote .rs{margin-left:50px;font-size:22px}
.person{display:flex;align-items:center;gap:14px;margin:24px 0 0 50px}
.person i{width:46px;height:46px;border-radius:50%;background:linear-gradient(135deg,#c9a98a,#8d6b52)}
.person b{font-size:15px;display:block}
.person small{font-size:11px;color:var(--muted)}
.pager{position:absolute;top:470px;left:0;width:1200px;text-align:center;font-size:10px;color:#ccc;letter-spacing:8px}

/* blogs */
.blogs{top:3720px;height:560px}
.posts{display:flex;gap:36px;justify-content:center;margin-top:50px}
.post{width:300px;background:var(--white);box-shadow:0 6px 20px rgba(0,0,0,.07);text-align:center}
.post .pic{height:240px}
.post .date{font-size:11px;color:var(--muted);margin-top:20px;letter-spacing:1px}
.post h4{font-size:13px;font-weight:700;margin:8px 24px 0}
.post p{font-size:11px;color:var(--muted);line-height:1.6;margin:8px 24px 24px}

/* newsletter */
.news{top:4300px;height:260px;background:var(--cream);text-align:center}
.news h2{font-size:34px;font-weight:600;margin-top:58px}
.news p{font-size:13px;color:var(--muted);margin-top:8px}
.news .form{display:flex;justify-content:center;gap:10px;margin-top:26px}
.news .field{width:380px;height:44px;border-radius:22px;background:var(--white);font-size:12px;color:#aaa;text-align:left;padding:14px 22px}

/* footer */
.footer{top:4560px;height:452px;background:linear-gradient(180deg,#fff,#f6f6f6)}
.cols{display:flex;gap:60px;padding:70px 0 0 130px}
.col{width:200px;font-size:12px;line-height:2;color:#555}
.col h5{font-size:13px;font-weight:700;color:var(--ink);margin-bottom:10px;letter-spacing:1px}
.social{display:flex;align-items:center;gap:10px}
.social i{width:20px;height:20px;border-radius:50%;background:var(--gold)}
.copyright{position:absolute;bottom:24px;left:0;width:1200px;text-align:center;font-size:11px;color:var(--muted)}
</style>
</head>
<body>

<div class="section topbar">Free shipping on all orders over $75 · Call 1-800-555-0147</div>

<header class="section nav">
  <div class="links"><span class="active">HOME</span><span>SHOP</span><span>ABOUT US</span></div>
  <div class="logo"><i></i>ZELLO CBD</div>
  <div class="links"><span>SEARCH</span><span>ACCOUNT</span><span>CART (0)</span></div>
</header>

<section class="section hero" role="img" aria-label="Woman relaxing with arms stretched in a bright bedroom beside a green plant">
  <div class="hero-copy">
    <small>WELCOME TO</small>
    <h1>ZELLO CBD</h1>
    <span class="btn">Shop Now</span>
  </div>
</section>

<section class="section about">
  <div class="shot" role="img" aria-label="Three dark dropper bottles of CBD oil with gold labels"></div>
  <div class="text">
    <h2>About The Zello<br><span>CBD Company</span></h2>
    <p>Zello CBD was born out of a love for a better life. Created to enable the extraordinary in all of us through the use of CBD. Made from clean hemp and crafted with care, our drops are designed to support calm, balance and everyday wellness for every lifestyle we serve.</p>
    <p>Providing high quality, complete CBD products that provide a lifestyle for people to get behind. Our products power the ones we love and every day we strive to share the benefits of a healthy life.</p>
  </div>
</section>

<section class="section brand">
  <div class="text">
    <h2><b>About</b> Our Brand</h2>
    <p>Zello is not your everyday CBD. Zello is a lifestyle. Zello is about incorporating into your daily routine to be the best you. Premium flavors, effective daily quality ingredients.</p>
  </div>
  <div class="shot" role="img" aria-label="Two glass vials of golden oil beside a hemp plant"></div>
</section>

<section class="section featured">
  <h2 class="title">Featured <b>Products</b></h2>
  <span class="arrow" style="left:50px">‹</span>
  <span class="arrow" style="right:50px">›</span>
  <div class="products">
    <div class="card"><div class="pic" role="img" aria-label="Dropper bottle of mint CBD oil"></div><div class="stars">★★★★★ <em>(86)</em></div><h4>Z Rise</h4><p>Sweet Mint Drops</p><div class="price">$64.99</div></div>
    <div class="card"><div class="pic" role="img" aria-label="Dropper bottle of cookie flavor CBD oil"><span class="btn">Add to Cart</span></div><div class="stars">★★★★★ <em>(71)</em></div><h4>Z Ease</h4><p>Ice Cream Cookie Drops</p><div class="price">$64.99</div></div>
    <div class="card"><div class="pic" role="img" aria-label="Dropper bottle of blueberry CBD oil"></div><div class="stars">★★★★★ <em>(58)</em></div><h4>Z Unwind</h4><p>Blueberry Lemonade Drops</p><div class="price">$64.99</div></div>
    <div class="card"><div class="pic" role="img" aria-label="Dropper bottle of strawberry CBD oil"></div><div class="stars">★★★★★ <em>(64)</em></div><h4>Z Bright</h4><p>Strawberry Drops</p><div class="price">$64.99</div></div>
  </div>
</section>

<section class="section why">
  <h2 class="title" style="margin-top:80px">Why <b>Zello CBD</b></h2>
  <svg width="1200" height="400" style="position:absolute;top:170px;left:0">
    <path d="M390 80 Q430 200 390 320" fill="none" stroke="#ccc" stroke-dasharray="4 5"/>
    <path d="M810 80 Q770 200 810 320" fill="none" stroke="#ccc" stroke-dasharray="4 5"/>
  </svg>
  <div role="img" aria-label="Three dark dropper bottles with gold labels" style="position:absolute;left:490px;top:260px;width:220px;height:240px;background:radial-gradient(ellipse 90px 110px at center,#2a2a2a 0%,#1f1f1f 70%,rgba(31,31,31,0) 100%)"></div>
  <div class="feat left" style="left:110px;top:226px">ZERO THC<span class="dot"></span></div>
  <div class="feat left" style="left:140px;top:346px">3RD PARTY LAB<br>TESTED<span class="dot"></span></div>
  <div class="feat left" style="left:110px;top:466px">FREE OF PESTICIDES<br>+ SOLVENTS<span class="dot"></span></div>
  <div class="feat" style="left:790px;top:226px"><span class="dot dark"></span>NON GMO</div>
  <div class="feat" style="left:760px;top:346px"><span class="dot dark"></span>BROAD SPECTRUM<br>HEMP CBD</div>
  <div class="feat" style="left:790px;top:466px"><span class="dot dark"></span>100% SOURCED +<br>MADE IN THE USA</div>
</section>

<section class="section reviews">
  <h2 class="title">Customer <b>Reviews</b></h2>
  <div class="quote">
    <span class="mark">“</span>
    <h3>I Love This Oil</h3>
    <p>Lorem ipsum dolor sit amet, consectetur adipiscing elit sed eiusmod tempor incididunt labore et dolore magna aliqua quis ipsum suspendisse ultrices gravida dolore magna aliqua.</p>
    <div class="stars rs">★★★★★</div>
    <div class="person"><i role="img" aria-label="Reviewer avatar"></i><div><b>Elena Marsh</b><small>@elenamarsh</small></div></div>
  </div>
  <div style="position:absolute;left:830px;top:150px;width:200px;text-align:center">
    <div role="img" aria-label="Dropper bottle of strawberry CBD oil" style="height:200px;border:1px solid var(--line);background:radial-gradient(ellipse 36px 72px at 50% 50%,#1f1f1f 0%,#2e2a22 60%,rgba(255,255,255,0) 100%),#fff"></div>
    <h4 style="font-size:14px;margin-top:12px">Z Bright</h4>
    <p style="font-size:12px;color:var(--muted)">Strawberry Drops</p>
    <span class="btn" style="font-size:11px;padding:9px 20px;margin-top:10px">Choose More</span>
  </div>
  <div class="pager">● ● ● ● ● ●</div>
</section>

<section class="section blogs">
  <h2 class="title">Blogs <b>and Offers</b></h2>
  <div class="posts">
    <div class="post"><div class="pic" role="img" aria-label="Woman meditating by a lake at sunset" style="background:linear-gradient(160deg,#b9d3e3,#e9c9a6)"></div><div class="date">FEBRUARY 28, 2020</div><h4>CONSECTETUR ADIPISCING SED DO EIUSMOD</h4><p>Lorem ipsum dolor sit amet consectetur adipiscing elit sed eiusmod tempor dolore.</p></div>
    <div class="post"><div class="pic" role="img" aria-label="Big sale promotion banner with sixty percent off" style="background:linear-gradient(160deg,#f3d35c,#e04f3b)"></div><div class="date">FEBRUARY 28, 2020</div><h4>CONSECTETUR ADIPISCING SED DO EIUSMOD</h4><p>Lorem ipsum dolor sit amet consectetur adipiscing elit sed eiusmod tempor dolore.</p></div>
    <div class="post"><div class="pic" role="img" aria-label="Person receiving a relaxing spa massage" style="background:linear-gradient(160deg,#e8d2bd,#a9805e)"></div><div class="date">FEBRUARY 28, 2020</div><h4>CONSECTETUR ADIPISCING SED DO EIUSMOD</h4><p>Lorem ipsum dolor sit amet consectetur adipiscing elit sed eiusmod tempor dolore.</p></div>
  </div>
</section>

<section class="section news">
  <h2>Join our Newsletter</h2>
  <p>Get the latest updates on new products and upcoming sales</p>
  <div class="form"><div class="field">Enter your email</div><span class="btn">Sign Up</span></div>
</section>

<footer class="section footer">
  <div class="cols">
    <div class="col"><h5>SITEMAP</h5>Why Zello CBD<br>Zello Ambassadors<br>Privacy Policy<br>Terms and Conditions<br>Shipping &amp; Returns<br>Contact Us</div>
    <div class="col"><h5>QUICK LINKS</h5>Shop<br>Blog<br>Reviews<br>About Us<br>Contact Us<br>Zello Cares</div>
    <div class="col"><h5>ADDRESS</h5>4418 Harbor Square<br>Fairview, TX 75069<br><br>+1 800 555 0147<br>hello@zellocbd.com</div>
    <div class="col"><h5>FOLLOW US</h5><div class="social"><i></i>COMMUNITY</div><div class="social"><i></i>GALLERY</div><div class="social"><i></i>BOARDS</div></div>
  </div>
  <div class="copyright">Copyright © 2020 Zello CBD. All Rights Reserved.</div>
</footer>

</body>
</html>
```